Business Card Design

We require a business card design for a law firm, our signature colours are maroon and cream. Our slogan is "From our family to yours", we would like the cards to be professional however feminine at the same time.

Industry/Entity Type

Business

Contact Information for Business Card

Helena Brackett & Associates Lawyers & Conveyancers, Helena Brackett LL.B. Principal Solicitor, 17 Quillon Street, Marrowdale NSW 2190

Logo styles of interest
Emblem Logo
Abstract Logo
Wordmark Logo

```html
<!DOCTYPE html>
<html lang="en">
<head>
<meta charset="utf-8">
<title>Helena Brackett &amp; Associates – Business Card</title>
<link rel="stylesheet" href="https://fonts.googleapis.com/css2?family=Dancing+Script:wght@400;500&family=Tinos&display=swap">
<style>
  :root {
    --maroon: #7f1a12;
    --maroon-soft: #8c2519;
    --cream: #fbf3d0;
  }
  html, body {
    margin: 0;
    padding: 0;
    overflow: hidden;
    background: var(--maroon);
  }
  .card {
    position: relative;
    width: 1200px;
    height: 726px;
    background: var(--maroon);
    color: var(--cream);
    overflow: hidden;
  }
  .emblem {
    position: absolute;
    left: 207px;
    top: 42px;
    width: 340px;
    height: 332px;
    background: var(--maroon-soft);
  }
  .firm-name {
    position: absolute;
    left: 51px;
    top: 392px;
    width: 600px;
    margin: 0;
    text-align: center;
    font-family: "Tinos", "Times New Roman", serif;
    font-weight: 400;
    font-size: 41px;
    line-height: 59px;
  }
  .slogan {
    position: absolute;
    left: 305px;
    top: 520px;
    margin: 0;
    font-family: "Dancing Script", cursive;
    font-size: 23px;
  }
  .contact {
    position: absolute;
    left: 712px;
    top: 425px;
    margin: 0;
    font-family: "Dancing Script", cursive;
    font-weight: 500;
    font-size: 46px;
    line-height: 61px;
    font-style: normal;
  }
  .contact span { display: block; white-space: nowrap; }
</style>
</head>
<body>
  <main class="card">
    <div class="emblem" role="img" aria-label="Firm emblem"></div>
    <h1 class="firm-name">Helena Brackett &amp; Associates<br>Lawyers &amp; Conveyancers</h1>
    <p class="slogan">From our family to yours</p>
    <address class="contact">
      <span class="contact-name">Helena Brackett LL.B.</span>
      <span class="contact-role">Principal Solicitor</span>
      <span class="contact-street">17 Quillon Street,</span>
      <span class="contact-suburb">Marrowdale NSW 2190</span>
    </address>
  </main>
</body>
</html>
```